Business Card Design for Kidvale (Hires out childrens play areas)

Looking to have a business card designed for a company we just bought. The company rents out childrens play areas.

I have uploaded a couple of examples of the kind of business card style I like. Here are two more examples:

https://quorvastudio.nz/project/bright-romp-branding/
https://imgvaultcdn.com/design_img/8841052/302917/302917_5518203_8841052_b73e19a2_image.jpg

I think a white card will be best due to all the colours in the logo.

Size we require: 3.75" x 2.25" (horizontally orientated) with a 0.125" bleed

Uploaded is two versions of our logo.

Details for the card:
1. My name: Liam Verster
2. Title: Managing Director
3. Phone no: 021 563 417
4. Email: liam@kidvale.co.nz
5. URL: www.kidvale.co.nz
6. Address:
PO Box 318625
Fernlea, Auckland

Let me know if you need anything else.

Target Market(s)

Hospitals, doctors surgeries, bed shops, etc.

Contact Information for Business Card

Details for the card:
1. My name: Liam Verster
3. Phone no: 021 563 417
5. URL: www.kidvale.co.nz
6. Address:
PO Box 318625
Fernlea, Auckland

Requirements
Should not have
• Not too busy.

```html
<!DOCTYPE html>
<html lang="en">
<head>
<meta charset="utf-8">
<title>Kidvale Business Card</title>
<link href="https://fonts.googleapis.com/css2?family=Lato:wght@400;700&display=swap" rel="stylesheet">
<style>
  :root {
    --stage: #999999;
    --card-white: #ffffff;
    --brand-purple: #7c2a90;
    --brand-magenta: #d61f8c;
    --name-blue: #1b57a8;
    --icon-blue: #1f5fb0;
    --ink: #2b2b2b;
    --rule: #9a9a9a;
  }
  * { margin: 0; padding: 0; box-sizing: border-box; }
  html, body { width: 1200px; height: 900px; overflow: hidden; }
  body {
    background: var(--stage);
    font-family: 'Lato', sans-serif;
    position: relative;
  }
  .card {
    position: absolute;
    top: 275px;
    width: 478px;
    height: 294px;
    overflow: hidden;
  }
  .card-front {
    left: 120px;
    background: var(--card-white);
    border-radius: 0 48px 0 48px;
  }
  .card-back {
    left: 606px;
    top: 274px;
    background: var(--brand-purple);
    border-radius: 48px 0 48px 0;
  }
  .brand-name {
    position: absolute;
    font-weight: 700;
    letter-spacing: 1px;
    line-height: 1;
  }
  .card-front .brand-name {
    right: 32px;
    top: 74px;
    font-size: 42px;
    color: var(--name-blue);
  }
  .card-back .brand-name {
    left: 0;
    right: 0;
    text-align: center;
    top: 125px;
    font-size: 64px;
    color: var(--card-white);
  }
  .person { position: absolute; left: 29px; top: 152px; }
  .person-name {
    font-size: 17px;
    font-weight: 400;
    color: var(--name-blue);
    letter-spacing: 0.3px;
  }
  .person-title { font-size: 13px; color: var(--ink); margin-top: 1px; }
  .divider {
    position: absolute;
    left: 29px;
    width: 418px;
    top: 197px;
    height: 1px;
    background: var(--rule);
  }
  .contact-list {
    position: absolute;
    left: 28px;
    top: 208px;
    list-style: none;
    font-size: 13px;
    color: var(--ink);
    line-height: 17px;
  }
  .contact-list li { display: flex; align-items: center; gap: 3px; }
  .contact-list svg { width: 11px; height: 11px; fill: var(--icon-blue); }
  .postal {
    position: absolute;
    right: 32px;
    top: 225px;
    text-align: right;
    font-size: 13px;
    line-height: 17px;
    color: var(--ink);
    font-style: normal;
  }
  .mascot-decoration {
    position: absolute;
    left: 0;
    top: 0;
    width: 230px;
    height: 294px;
    background: radial-gradient(ellipse at 30% 95%, rgba(214,31,140,0.85), rgba(124,42,144,0) 65%),
                radial-gradient(ellipse at 45% 35%, rgba(150,60,170,0.6), rgba(124,42,144,0) 70%);
  }
</style>
</head>
<body>
  <section class="card card-front">
    <div class="brand-name">Kidvale</div>
    <div class="person">
      <div class="person-name">LIAM VERSTER</div>
      <div class="person-title">Managing Director</div>
    </div>
    <div class="divider"></div>
    <ul class="contact-list">
      <li>
        <svg viewBox="0 0 12 12" aria-hidden="true"><path d="M1 4c0-2 2-3 5-3s5 1 5 3v1H8.5V4h-5v1H1zM2.5 6h7l1 5h-9z"/></svg>
        021 563 417
      </li>
      <li>
        <svg viewBox="0 0 12 12" aria-hidden="true"><path d="M1 2.5h10v7H1z M1.5 3l4.5 3.5L10.5 3" stroke="#fff" stroke-width="0.9"/></svg>
        liam@kidvale.co.nz
      </li>
      <li>
        <svg viewBox="0 0 12 12" aria-hidden="true"><circle cx="6" cy="6" r="5"/><path d="M1 6h10M6 1c-2 2.5-2 7.5 0 10M6 1c2 2.5 2 7.5 0 10" stroke="#fff" stroke-width="0.7" fill="none"/></svg>
        www.kidvale.co.nz
      </li>
    </ul>
    <address class="postal">PO Box 318625<br>Fernlea, Auckland</address>
  </section>

  <section class="card card-back">
    <div class="mascot-decoration" role="img" aria-label="Faint enlarged brand mascot decoration in purple and magenta tones"></div>
    <div class="brand-name">Kidvale</div>
  </section>
</body>
</html>
```